依頼詳細
※ワイヤーフレームは以下よりダウンロードしてください
https://52.filokura.example/0714-e2f19c7a0d4b8e61a3c5f0d9b7e24a6c1f

※画像素材はピクソラフォトを使用してください

■サイトマップ
1 TOP
2 会社情報
3 企業理念
4 代表あいさつ
5 社員紹介(一覧)
6 プライバシーポリシー
7 事業内容
8 ツアーの流れ
9 採用情報
10 目的別の旅行先(一覧)
11 目的別の旅行先(詳細)
12 日本の旅行先(一覧)
13 日本の旅行先(詳細)
14 コラム(一覧)
15 コラム(詳細)
16 よくある質問(一覧)
17 お客様の声(一覧)
18 お客様の声(詳細)
19 お問い合わせ

■参考サイト(※現行サイト、ポータルサイトなど)
・現行サイト
https://www.kumotabi-ryoko.co.jp/

・参考サイト
https://www.hoshizoratrips.jp/company/
└レイアウトを参考にしていただきたいです。

https://www.lodgeqmr.com/lumieresquare/
└上記サイトのようにMVをフルディスプレイにして、
飛行機の写真を使用していただきたいです。

■カラー
白ベースで、ポイントや背景画像に青系を使用してください。
以下のサイトの色味を参考にしてください。
https://www.sorafune-tec.co.jp/

■フォントについて
・無料で使えるフォントで作成お願い致します
・OSに紐づくフォントの使用は控えていただければと思います (ヒラギノなど)

■文章について
・可能な限り「ダミーテキスト」を繰り返した文字の配置は避けて頂きたいです

■ワイヤーフレーム
こちらを参考にしていただきたいです。
デザインなどはお任せいたします。
ページ数
1ページ
希望イメージ
シンプル 複雑
単色 カラフル
暗い 明るい
日常 高級
遊び心 厳粛
未来的 伝統的
女性的 男性的
希望する色
青系
納品ファイル
• イラストレーター形式 (.ai)
• フォトショップ形式 (.psd)
補足説明
◆素材について
Pixora Photo画像をご使用ください。
その際、通常アセットでダウンロード出来る画像のみを使用してください。
Pixora Photo以外の素材を使用する際には、
必ず無料で提供いただける物のみご使用ください。

◆ワイヤーフレームについて
絶対に厳守していただく必要はございません。
デザイン的にこちらの方が良いなどあれば、
そちらを採用してください

◆サイズについて
TOPデザイン自体の画像サイズは、横幅1300pxで提案をお願いできますと幸いです。(縦幅の制限はございません)

※通常業務へ支障が出るため、店舗へのお電話はお控え下さい。
もう少し提案を見させて頂きたい為、期間を延長いたします。
皆様のご提案をお待ちしております。

```html
<!DOCTYPE html>
<html lang="ja">
<head>
<meta charset="utf-8">
<title>クモタビツアー | 旅行のご予約</title>
<link rel="stylesheet" href="https://fonts.googleapis.com/css2?family=Noto+Sans+JP:wght@400;500;700;900&family=Montserrat:ital,wght@0,500;0,700;1,800&display=swap">
<style>
:root{
  --blue:#0a4fb3;
  --blue-deep:#063b8f;
  --navy:#0a3680;
  --sky-top:#2f7fd6;
  --sky-low:#cfe3f6;
  --gold-a:#c7a25a;
  --gold-b:#a27b2f;
  --gray-bg:#f2f2f2;
  --ink:#222;
  --muted:#777;
  --white:#fff;
}
*{box-sizing:border-box;margin:0;padding:0}
html,body{width:1200px;height:5332px;overflow:hidden}
body{font-family:"Noto Sans JP",sans-serif;color:var(--ink);background:var(--white);position:relative}
.en{font-family:"Montserrat",sans-serif}
section,header,footer{position:relative;width:1200px;overflow:hidden}

/* hero */
.hero{height:680px;background:linear-gradient(180deg,var(--sky-top) 0%,#6fa9e4 40%,var(--sky-low) 75%,#3a78c8 100%)}
.hero-photo{position:absolute;inset:0}
.hero-band{position:absolute;inset:0}
.brand{position:absolute;left:28px;top:20px;display:flex;align-items:center;gap:10px;color:var(--white)}
.brand-dot{width:22px;height:22px;border-radius:50%;background:var(--white)}
.brand-name{font-size:17px;font-weight:700;letter-spacing:.05em}
.brand-sub{position:absolute;left:28px;top:52px;color:var(--white);font-size:10px;line-height:1.5}
.gnav{position:absolute;right:20px;top:28px;display:flex;gap:34px;color:var(--white);font-size:13px;font-weight:500}
.hero-copy{position:absolute;left:40px;top:320px;color:var(--white)}
.hero-copy .big{font-family:"Montserrat",sans-serif;font-style:italic;font-weight:800;font-size:104px;line-height:1;letter-spacing:.02em}
.hero-copy .tag{font-size:16px;font-weight:700;margin:14px 0 14px 6px;letter-spacing:.1em}
.scroll{position:absolute;left:10px;top:560px;writing-mode:vertical-rl;font-size:9px;color:var(--white);letter-spacing:.2em}
.hero-tel{position:absolute;right:24px;top:564px;color:var(--white);display:flex;align-items:baseline;gap:14px}
.hero-tel small{font-size:11px}
.hero-tel b{font-family:"Montserrat",sans-serif;font-size:22px;font-weight:700}
.hero-cta{position:absolute;right:0;top:608px;width:370px;height:44px;background:linear-gradient(90deg,var(--gold-a),var(--gold-b));color:var(--white);display:flex;align-items:center;justify-content:center;gap:10px;font-size:14px;font-weight:700}
.circle-arrow{width:20px;height:20px;border:1px solid currentColor;border-radius:50%;display:inline-flex;align-items:center;justify-content:center}

/* buttons */
.btn-more{display:flex;align-items:center;justify-content:center;gap:40px;width:280px;height:44px;margin:0 auto;background:linear-gradient(90deg,var(--gold-a),var(--gold-b));color:var(--white);font-family:"Montserrat",sans-serif;font-size:12px;font-weight:700;letter-spacing:.15em}

/* headings */
.sec-title{text-align:center}
.sec-title h2{font-size:36px;font-weight:700;letter-spacing:.06em}
.sec-title p{font-family:"Montserrat",sans-serif;font-size:11px;letter-spacing:.2em;color:var(--muted);margin-top:6px}

/* news */
.news{height:380px}
.news-box{position:absolute;left:176px;top:84px;width:850px;display:flex;align-items:center}
.news-label{width:170px;height:120px;border:1px solid #ccc;display:flex;flex-direction:column;align-items:center;justify-content:center}
.news-label h2{font-size:18px;font-weight:700}
.news-label p{font-size:9px;color:var(--muted);letter-spacing:.2em;margin-top:4px}
.news-list{list-style:none;margin-left:40px}
.news-list li{display:flex;align-items:center;gap:14px;height:34px;font-size:13px}
.news-list time{font-family:"Montserrat",sans-serif;font-size:11px;width:84px}
.news-cat{background:var(--ink);color:var(--white);font-size:10px;padding:2px 10px}
.news .btn-more{position:absolute;left:460px;top:282px}

/* booking */
.booking{height:1210px;background:var(--gray-bg)}
.booking .sec-title{padding-top:20px}
.dest-grid{position:absolute;left:48px;top:280px;display:grid;grid-template-columns:repeat(3,352px);column-gap:24px;row-gap:22px}
.dest{background:var(--white);height:232px;box-shadow:0 2px 6px rgba(0,0,0,.06)}
.dest-photo{height:178px}
.dest-name{height:54px;display:flex;align-items:center;justify-content:space-between;padding:0 14px 0 18px;font-family:"Montserrat",sans-serif;font-weight:800;font-style:italic;font-size:20px}
.dest-name .circle-arrow{width:26px;height:26px;color:#444}
.dest-name.two{font-size:13px;line-height:1.1}
.booking .btn-more{position:absolute;left:460px;top:1078px}

/* services */
.services{height:1060px;background:var(--blue)}
.services .sec-title{position:relative;padding-top:120px;color:var(--white)}
.services .sec-title p{color:#cfe0ff}
.svc-grid{position:absolute;left:160px;top:246px;display:grid;grid-template-columns:repeat(3,240px);column-gap:80px;row-gap:52px}
.svc{text-align:center;color:var(--white)}
.svc-photo{width:232px;height:232px;border-radius:50%;margin:0 auto}
.svc p{font-size:14px;font-weight:500;margin-top:18px}
.services .btn-more{position:absolute;left:460px;top:930px}

/* media */
.media{height:730px}
.media .sec-title{padding-top:100px}
.media-row{position:absolute;left:64px;top:270px;width:1072px;height:360px;display:grid;grid-template-columns:repeat(3,1fr)}
.media-card{position:relative;display:flex;flex-direction:column;align-items:center;justify-content:center;color:var(--white)}
.media-card h3{font-size:24px;font-weight:700;text-shadow:0 1px 6px rgba(0,0,0,.4)}
.media-card p{font-family:"Montserrat",sans-serif;font-size:10px;letter-spacing:.2em;margin-top:4px}

/* faq */
.faq{height:630px;background:var(--gray-bg)}
.faq .sec-title{padding-top:100px}
.faq-list{position:absolute;left:300px;top:250px;width:600px;list-style:none}
.faq-list li{padding:12px 0;border-bottom:1px solid #ccc}
.faq-list .row{display:flex;gap:14px;font-size:12px;height:26px;align-items:center}
.faq-list .q{font-family:"Montserrat",sans-serif;font-weight:700;color:var(--blue)}
.faq-list .a{font-family:"Montserrat",sans-serif;font-weight:700;color:var(--gold-b)}
.faq .btn-more{position:absolute;left:460px;top:510px}

/* strip + footer */
.strip{height:70px;background:var(--blue);color:var(--white);display:flex;align-items:center;justify-content:center;font-size:16px;font-weight:700;letter-spacing:.05em}
.site-footer{height:572px;background:var(--navy);color:var(--white)}
.f-brand{position:absolute;left:120px;top:46px}
.f-brand .brand{position:static}
.f-info{position:absolute;left:120px;top:110px;font-size:11px;line-height:1.9}
.f-btn{position:absolute;left:120px;top:340px;width:240px;height:34px;border:1px solid var(--white);font-size:11px;display:flex;align-items:center;justify-content:center}
.f-nav{position:absolute;top:50px;list-style:none;font-size:12px;line-height:2.4}
.f-nav.c1{left:600px}.f-nav.c2{left:760px}.f-nav.c3{left:940px}
.copy{position:absolute;left:0;right:0;top:520px;text-align:center;font-size:10px;color:#c8d6f0}
.pagetop{position:absolute;right:16px;top:514px;width:24px;height:24px;background:var(--white);color:var(--navy);display:flex;align-items:center;justify-content:center;font-size:10px}
</style>
</head>
<body>

<header class="hero">
  <div class="hero-photo" role="img" aria-label="青空を飛ぶ旅客機と雲海の写真"></div>
  <svg class="hero-band" width="1200" height="680" viewBox="0 0 1200 680" aria-hidden="true">
    <polygon points="0,680 0,600 700,680" fill="#ffffff"/>
    <polygon points="620,680 1200,420 1200,680" fill="#0a4fb3" opacity=".85"/>
    <polygon points="820,680 1200,500 1200,680" fill="#063b8f"/>
  </svg>
  <div class="brand"><span class="brand-dot"></span><span class="brand-name">クモタビツアー</span></div>
  <p class="brand-sub">関西発の航空機で行く手軽な旅行は<br>クモタビツーリストへ</p>
  <nav class="gnav"><span>会社情報</span><span>事業内容</span><span>ツアーの流れ</span><span>採用情報</span><span>日本の旅行先</span><span>お問い合わせ</span></nav>
  <div class="hero-copy">
    <div class="big">ENJOY</div>
    <p class="tag">あなたの旅を丁寧にサポートする会社</p>
    <div class="big">THE TRIP</div>
  </div>
  <p class="scroll en">SCROLL</p>
  <div class="hero-tel"><small>お電話でのお問い合わせ</small><b>06-4820-3175</b></div>
  <div class="hero-cta">今すぐ旅行に行く <span class="circle-arrow"><svg width="8" height="8" viewBox="0 0 8 8"><path d="M2 1l3 3-3 3" stroke="#fff" fill="none"/></svg></span></div>
</header>

<section class="news">
  <div class="news-box">
    <div class="news-label"><h2>新着情報</h2><p class="en">NEWS</p></div>
    <ul class="news-list">
      <li><time>2020.10.07</time><span class="news-cat">お知らせ</span>秋の北海道ツアーの受付を開始しました。お早めにご予約ください</li>
      <li><time>2020.10.01</time><span class="news-cat">お知らせ</span>年末年始の営業日についてのご案内を掲載いたしました</li>
      <li><time>2020.09.24</time><span class="news-cat">お知らせ</span>沖縄離島めぐりの新プランを追加しました。詳細はこちら</li>
    </ul>
  </div>
  <a class="btn-more">VIEW MORE <span>›</span></a>
</section>

<section class="booking">
  <div class="sec-title" style="padding-top:30px"><h2>今すぐ旅行を予約する</h2><p>RESERVE</p></div>
  <div class="dest-grid">
    <div class="dest"><div class="dest-photo" role="img" aria-label="北海道の丘と空の風景写真" style="background:linear-gradient(180deg,#7fb2e6,#6f9b5c)"></div><div class="dest-name">HOKKAIDO<span class="circle-arrow">›</span></div></div>
    <div class="dest"><div class="dest-photo" role="img" aria-label="沖縄のシーサーと海の写真" style="background:linear-gradient(180deg,#9cc9ec,#3aa6b8)"></div><div class="dest-name">OKINAWA<span class="circle-arrow">›</span></div></div>
    <div class="dest"><div class="dest-photo" role="img" aria-label="九州の夜の屋台街の写真" style="background:linear-gradient(180deg,#4a2c1c,#c47a2e)"></div><div class="dest-name">KYUSHU<span class="circle-arrow">›</span></div></div>
    <div class="dest"><div class="dest-photo" role="img" aria-label="東京タワーと街並みの写真" style="background:linear-gradient(180deg,#a9cdee,#8a8f99)"></div><div class="dest-name">TOKYO<span class="circle-arrow">›</span></div></div>
    <div class="dest"><div class="dest-photo" role="img" aria-label="関西の寺院と夕景の写真" style="background:linear-gradient(180deg,#e7a35a,#6a3a24)"></div><div class="dest-name">KANSAI<span class="circle-arrow">›</span></div></div>
    <div class="dest"><div class="dest-photo" role="img" aria-label="東北のねぶた祭の写真" style="background:linear-gradient(180deg,#b8281e,#e3a23a)"></div><div class="dest-name">TOHOKU<span class="circle-arrow">›</span></div></div>
    <div class="dest"><div class="dest-photo" role="img" aria-label="四国の海にかかる大橋の写真" style="background:linear-gradient(180deg,#a8cff0,#4f8fbf)"></div><div class="dest-name">SHIKOKU<span class="circle-arrow">›</span></div></div>
    <div class="dest"><div class="dest-photo" role="img" aria-label="海に立つ朱色の鳥居の写真" style="background:linear-gradient(180deg,#b9d9f2,#5f8fb3)"></div><div class="dest-name">SANIN SANYO<span class="circle-arrow">›</span></div></div>
    <div class="dest"><div class="dest-photo" role="img" aria-label="温泉の湯けむりの写真" style="background:linear-gradient(180deg,#d8cbb4,#8c6b46)"></div><div class="dest-name two">HOT SPRING<br>SPECIAL FEATURE<span class="circle-arrow">›</span></div></div>
  </div>
  <a class="btn-more" style="font-family:'Noto Sans JP',sans-serif;letter-spacing:.05em">ダイナミックパッケージへ <span>›</span></a>
</section>

<section class="services">
  <svg style="position:absolute;left:0;top:0" width="1200" height="300" viewBox="0 0 1200 300" aria-hidden="true">
    <polygon points="0,0 1200,0 1200,60 0,220" fill="#0d5cc7"/>
    <polygon points="600,0 1200,0 1200,180" fill="#1a6ad6" opacity=".7"/>
  </svg>
  <div class="sec-title"><h2>事業内容</h2><p>SERVICES</p></div>
  <div class="svc-grid">
    <div class="svc"><div class="svc-photo" role="img" aria-label="雲の上を飛ぶ飛行機の写真" style="background:linear-gradient(160deg,#e8eef6,#5d86c2)"></div><p>ダイナミックパッケージ</p></div>
    <div class="svc"><div class="svc-photo" role="img" aria-label="空港のスーツケースの写真" style="background:linear-gradient(160deg,#f0ead8,#e3b53a)"></div><p>国内・海外旅行</p></div>
    <div class="svc"><div class="svc-photo" role="img" aria-label="空港を歩くビジネス客の写真" style="background:linear-gradient(160deg,#cfd8e2,#3c5a7e)"></div><p>法人出張</p></div>
    <div class="svc"><div class="svc-photo" role="img" aria-label="打ち合わせをするスタッフの写真" style="background:linear-gradient(160deg,#f2f2f2,#9aa6b2)"></div><p>ブランドアドバイス</p></div>
    <div class="svc"><div class="svc-photo" role="img" aria-label="旅行を楽しむ人々の写真" style="background:linear-gradient(160deg,#e6e2da,#8d7a64)"></div><p>インセンティブツアー</p></div>
    <div class="svc"><div class="svc-photo" role="img" aria-label="研修会場の写真" style="background:linear-gradient(160deg,#dde6ef,#4c6d93)"></div><p>海外研修旅行</p></div>
  </div>
  <a class="btn-more">VIEW MORE <span>›</span></a>
</section>

<section class="media">
  <div class="sec-title"><h2>自社メディア</h2><p>MEDIA</p></div>
  <div class="media-row">
    <div class="media-card" role="img" aria-label="五重塔と山の風景写真" style="background:linear-gradient(180deg,#d27a5a,#5a3a3a)"><h3>日本の旅行先</h3><p>TRAVEL IN JAPAN</p></div>
    <div class="media-card" role="img" aria-label="寿司の写真" style="background:linear-gradient(180deg,#c9826a,#4a2a22)"><h3>目的別に旅行先</h3><p>PURPOSE</p></div>
    <div class="media-card" role="img" aria-label="ノートパソコンで作業する手元の写真" style="background:linear-gradient(180deg,#9aa3a8,#4b5257)"><h3>コラム</h3><p>COLUMN</p></div>
  </div>
</section>

<section class="faq">
  <div class="sec-title"><h2>よくある質問</h2><p>Q&amp;A</p></div>
  <ul class="faq-list">
    <li><div class="row"><span class="q">Q</span>ツアーの予約はいつまでに申し込めばよいですか？</div><div class="row"><span class="a">A</span>出発日の七日前までお申し込みいただけます。</div></li>
    <li><div class="row"><span class="q">Q</span>キャンセル料はいつから発生しますか？</div><div class="row"><span class="a">A</span>出発日の二十日前から規定の料金がかかります。</div></li>
    <li><div class="row"><span class="q">Q</span>法人の出張手配にも対応していますか？</div><div class="row"><span class="a">A</span>はい、専任スタッフがご要望に合わせて手配いたします。</div></li>
  </ul>
  <a class="btn-more">VIEW MORE <span>›</span></a>
</section>

<div class="strip">関西発のソラフネ航空で行く手軽格安な旅のご予約はクモタビツーリストへ</div>

<footer class="site-footer">
  <div class="f-brand"><div class="brand"><span class="brand-dot"></span><span class="brand-name">クモタビツアー</span></div></div>
  <div class="f-info">
    【会社名】クモタビツアー<br>株式会社クモタビツーリスト<br><br>
    〒540-0000<br>大阪府大阪市中央区雲野町2-8-14<br><br>
    TEL：06-4820-3175<br>営業時間<br>平日 10:00〜18:00<br>土曜 10:00〜15:00（日曜・祝日休業）
  </div>
  <div class="f-btn">大阪府知事登録旅行業 第0000号</div>
  <ul class="f-nav c1"><li>TOP</li><li>会社情報</li><li>事業内容</li><li>ツアーの流れ</li><li>採用情報</li><li>お客様の声</li><li>お問い合わせ</li></ul>
  <ul class="f-nav c2"><li>日本の旅行先</li><li>目的別の旅行先</li><li>コラム</li></ul>
  <ul class="f-nav c3"><li>企業理念</li><li>代表あいさつ</li><li>社員紹介</li><li>プライバシーポリシー</li><li>よくある質問</li></ul>
  <p class="copy en">Copyright © 2020 KUMOTABI TOURIST. All rights reserved.</p>
  <div class="pagetop">▲</div>
</footer>

</body>
</html>
```